Harbor Lantern Diagnostics
Stationary/Business Card
Project: Harbor Lantern Diagnostics
Harbor Lantern Diagnostics - Medical
Creative Brief
Use specific fonts
Font like in the uploaded pic (playing card)
Cutting-Edge
Marlo Quist
Chief Executive Officer
417 W Dunmore A Lubbock, Tx
marlo_047@quillpost.example
harborlanterndiagnostics.example
For the stationary I uploaded some ideas of how I would love for it to look like.
For the front and the back design of the business card, I have uploaded
orvell512 orvell512
I've already picked the winner for the logo but I'm still waiting on the finished product from the designer.

```html
<!DOCTYPE html>
<html lang="en">
<head>
<meta charset="utf-8">
<title>Harbor Lantern Diagnostics – Business Card</title>
<link rel="stylesheet" href="https://fonts.googleapis.com/css2?family=Open+Sans:wght@300;400;600;700&display=swap">
<style>
  :root {
    --backdrop: #e4e4e6;
    --card: #ffffff;
    --ink: #3a3a3a;
    --ink-soft: #6b6b6b;
    --gold-light: #efd21c;
    --gold-deep: #c9a20e;
    --red-light: #d8281e;
    --red-deep: #a3110c;
    --white: #ffffff;
  }
  * { box-sizing: border-box; margin: 0; padding: 0; }
  html, body {
    width: 1200px; height: 883px; overflow: hidden;
    background: var(--backdrop);
    font-family: "Open Sans", Arial, sans-serif;
  }
  .canvas { position: relative; width: 1200px; height: 883px; }

  .card {
    position: absolute;
    width: 560px; height: 320px;
    background: var(--card);
    border-radius: 26px;
    overflow: hidden;
    box-shadow: 0 6px 18px rgba(0,0,0,0.12);
  }
  .card-back { left: 570px; top: 80px; }
  .card-front { left: 70px; top: 480px; }

  /* Back */
  .brand {
    position: absolute; left: 90px; top: 70px; width: 240px;
    text-align: center;
  }
  .brand-name {
    font-size: 9px; font-weight: 600; letter-spacing: 1.5px;
    text-transform: uppercase; color: var(--ink-soft);
    white-space: nowrap;
  }
  .brand-mark {
    width: 84px; height: 84px; margin: 14px auto 0;
    border-radius: 50%; background: var(--red-deep);
  }
  .back-band {
    position: absolute; left: 330px; top: 96px; right: 0; height: 76px;
    display: flex;
  }
  .back-band .gold {
    flex: 0 0 170px;
    background: linear-gradient(180deg, var(--gold-light), var(--gold-deep));
    display: flex; align-items: center; justify-content: center;
    color: var(--white); font-size: 7px; letter-spacing: 0.3px;
    white-space: nowrap;
  }
  .back-band .red {
    flex: 1;
    background: linear-gradient(180deg, var(--red-light), var(--red-deep));
  }

  /* Front */
  .identity {
    position: absolute; left: 100px; top: 44px; width: 360px; text-align: center;
  }
  .person-name {
    font-size: 28px; font-weight: 300; letter-spacing: 0.5px; color: var(--ink);
    text-transform: uppercase; white-space: nowrap;
  }
  .person-name strong { font-weight: 700; }
  .person-role {
    font-size: 10px; font-weight: 600; letter-spacing: 1.5px;
    color: var(--ink-soft); text-transform: uppercase; margin-top: 2px;
  }
  .contact-band {
    position: absolute; left: 0; top: 128px; width: 100%; height: 96px;
    display: flex;
  }
  .contact-band .phone {
    flex: 0 0 230px;
    background: linear-gradient(180deg, var(--gold-light), var(--gold-deep));
    padding: 20px 0 0 64px;
  }
  .contact-band .web {
    flex: 1;
    background: linear-gradient(180deg, var(--red-light), var(--red-deep));
    padding: 20px 0 0 26px;
  }
  .contact-label {
    font-size: 12px; font-weight: 600; color: var(--white);
    text-transform: uppercase; letter-spacing: 1px;
  }
  .contact-line {
    font-size: 11px; color: var(--white); line-height: 1.45;
    text-transform: uppercase; white-space: nowrap;
  }
  .address {
    position: absolute; left: 0; width: 100%; top: 244px; text-align: center;
    font-size: 11px; letter-spacing: 1px; color: var(--ink-soft);
    text-transform: uppercase; line-height: 1.5;
  }
  .address .city { font-weight: 600; }
</style>
</head>
<body>
<main class="canvas">

  <section class="card card-back" aria-label="Business card back">
    <div class="brand">
      <p class="brand-name">Harbor Lantern Diagnostics</p>
      <div class="brand-mark"></div>
    </div>
    <div class="back-band">
      <div class="gold">harborlanterndiagnostics.example</div>
      <div class="red"></div>
    </div>
  </section>

  <section class="card card-front" aria-label="Business card front">
    <header class="identity">
      <h1 class="person-name">Marlo <strong>Quist</strong></h1>
      <p class="person-role">Chief Executive Officer</p>
    </header>
    <div class="contact-band">
      <div class="phone">
        <p class="contact-label">Phone &amp; Fax</p>
        <p class="contact-line">+100 555 0142</p>
        <p class="contact-line">+100 555 0187</p>
      </div>
      <div class="web">
        <p class="contact-label">Email &amp; Web</p>
        <p class="contact-line">marlo_047@quillpost.example</p>
        <p class="contact-line">harborlanterndiagnostics.example</p>
      </div>
    </div>
    <footer class="address">
      <p>417 W Dunmore A</p>
      <p class="city">Lubbock, Tx</p>
    </footer>
  </section>

</main>
</body>
</html>
```